Postcard Design

Need postcard design for dental office. The doctor is returning to the office after a few months medical leave and he wants a postcard to be mailed to patients and families in the surrounding area to create new patients. We have attached a rough sketch of the information we would like to include on the postcard along with color selection but are open to additional artwork or design to improve the overall look. We are also including a photo of the dentist for the front of the postcard. We plan to have the metered postage through Plentomark if possible so please let me know how that works because I'm assuming that will need to be included in the design. I am also attaching a sample of a postcard that the dentist received in the mail from a Corbridge doctor and would like his postcard to resemble this layout. The postcard needs to 8.5 x 5.5; I believe this is called the oversized selection for Plentomark and we are planning to have them do the printing. Please verify you did receive four attached files including photo, front sketch, back sketch, and actual postcard example.

Thank you,
Marlene Tofsky

```html
<!DOCTYPE html>
<html lang="en">
<head>
<meta charset="utf-8">
<title>General Dentist Postcard</title>
<link href="https://fonts.googleapis.com/css2?family=Roboto+Condensed:wght@400;700&display=swap" rel="stylesheet">
<style>
  :root {
    --navy: #1d3a8a;
    --blue: #1f5fb0;
    --blue-deep: #17418f;
    --sky: #a9dbe6;
    --green: #76bd43;
    --ink: #2b3682;
    --paper: #ffffff;
    --paper-grey: #e4e6ea;
  }
  * { margin: 0; padding: 0; box-sizing: border-box; }
  html, body { width: 1200px; height: 772px; overflow: hidden; background: var(--paper); }
  .postcard {
    position: relative; width: 1200px; height: 772px; overflow: hidden;
    font-family: "Roboto Condensed", "Arial Narrow", sans-serif;
    background: linear-gradient(180deg, var(--paper) 40%, var(--paper-grey) 78%, var(--paper) 100%);
  }
  .waves { position: absolute; inset: 0; }
  .portrait-frame {
    position: absolute; left: 82px; top: 80px; width: 438px; height: 448px;
    background: var(--paper); padding: 8px;
    box-shadow: 3px 5px 10px rgba(0,0,0,.35);
  }
  .portrait {
    width: 100%; height: 100%;
    background: linear-gradient(180deg, #e9e8e6 0%, #d9cfc8 45%, #2a2a30 80%, #1f1f24 100%);
  }
  .specialty-tab {
    position: absolute; left: 618px; top: 0; width: 510px; height: 96px;
    background: var(--green); border-radius: 0 0 12px 12px;
    color: var(--paper); font-weight: 700; font-size: 49px;
    display: flex; align-items: center; justify-content: center; letter-spacing: .5px;
  }
  .intro {
    position: absolute; left: 560px; width: 626px; top: 124px; text-align: center;
    color: var(--paper); font-weight: 700; font-size: 28px;
  }
  .doctor-name {
    position: absolute; left: 560px; width: 626px; top: 190px; text-align: center;
    color: var(--paper); font-weight: 700; font-size: 48px;
  }
  .credentials {
    position: absolute; right: 160px; top: 258px;
    color: var(--paper); font-size: 25px; letter-spacing: 1px;
  }
  .divider {
    position: absolute; left: 686px; top: 296px; width: 372px; height: 2px; background: var(--paper);
  }
  .phone-main {
    position: absolute; left: 560px; width: 626px; top: 314px; text-align: center;
    color: var(--paper); font-weight: 700; font-size: 40px;
  }
  .address {
    position: absolute; left: 680px; top: 472px;
    color: var(--ink); font-size: 28px; line-height: 40px; font-style: normal;
  }
  .footer-band {
    position: absolute; left: 0; top: 605px; width: 1200px; height: 117px;
    background: linear-gradient(180deg, var(--blue-deep), var(--navy));
    border-top: 5px solid #4fa3dc; border-bottom: 4px solid #4fa3dc;
  }
  .footer-headline {
    position: absolute; left: 38px; top: 36px;
    color: var(--paper); font-weight: 700; font-size: 45px;
  }
  .footer-contact {
    position: absolute; left: 682px; top: 22px;
    color: var(--paper); font-size: 28px; line-height: 42px;
  }
  .footer-contact strong { font-weight: 700; }
</style>
</head>
<body>
<div class="postcard">
  <svg class="waves" width="1200" height="772" viewBox="0 0 1200 772" aria-hidden="true">
    <defs>
      <linearGradient id="headerBlue" x1="0" y1="0" x2="1" y2="1">
        <stop offset="0" stop-color="#1b3f8f"/>
        <stop offset=".6" stop-color="#1f64b4"/>
        <stop offset="1" stop-color="#1b3f8f"/>
      </linearGradient>
    </defs>
    <path d="M0,0 H1200 V300 C1120,390 1000,440 880,425 C760,410 640,330 520,275 C400,220 200,160 0,170 Z" fill="url(#headerBlue)"/>
    <path d="M0,200 C200,190 400,250 520,300 C640,352 760,430 880,445 C1000,458 1120,410 1200,330" fill="none" stroke="#2a54a3" stroke-width="22"/>
    <path d="M0,240 C200,230 400,285 520,330 C640,375 760,448 880,462 C1000,474 1120,435 1200,360" fill="none" stroke="var(--green)" stroke-width="8"/>
    <path d="M0,262 C200,255 400,305 520,350 C640,395 760,465 880,478 C1000,490 1120,455 1200,385" fill="none" stroke="var(--sky)" stroke-width="10"/>
    <path d="M0,300 C120,290 220,300 300,320 L300,380 C220,360 120,345 0,360 Z" fill="var(--green)" opacity=".9"/>
  </svg>

  <div class="portrait-frame">
    <div class="portrait" role="img" aria-label="Portrait photo of the dentist in a dark suit and tie"></div>
  </div>

  <div class="specialty-tab">GENERAL DENTIST</div>
  <p class="intro">Now Accepting Established and New Patients</p>
  <h1 class="doctor-name">Dr. Alden P. Marsh</h1>
  <p class="credentials">D.D.S., F.A.G.D.</p>
  <div class="divider"></div>
  <p class="phone-main">770-555-0182</p>

  <address class="address">
    Brennford<br>
    4820-B Harlow Pkwy, Suite B<br>
    Brennford, GA 30199
  </address>

  <div class="footer-band">
    <p class="footer-headline">NOW ACCEPTING PATIENTS</p>
    <p class="footer-contact">For More Information, Please Call<br><strong>770-555-0182</strong> or Visit <strong>DrAldenMarsh.com</strong></p>
  </div>
</div>
</body>
</html>
```